Flyer-Design für unabhängige Vermögensverwaltung
Sehr seriöser und zuverlässiger Partner. Werden in Zukunft gerne erneut mit Ihm zusammenarbeiten.
Zielgruppe
Wir sind eine unabhängige Vermögensverwaltung.
Aufgabenstellung
Es soll ein bestehender Flyer nur leicht modifiziert werden.
Alle den Text und die Bilder stellen wir zur Verfügung.
Der Flyer soll wahrscheinlich bei Drucklinde gedruckt werden.
Es wäre daher wichtig, dass die Farbe so gewählt wird, dass es identisch zu den noch vorhandenen Exemplaren ist.
In Zukunft sollen auch weitere Flyer komplett von 0 geplant werden.

```html
<!DOCTYPE html>
<html lang="de">
<head>
<meta charset="utf-8">
<title>SOLITAR Vermögensverwaltung – Flyer Innenseite</title>
<link href="https://fonts.googleapis.com/css2?family=Crimson+Pro:wght@400&family=Barlow+Semi+Condensed:wght@300;500&display=swap" rel="stylesheet">
<style>
  :root {
    --navy: #1c358f;
    --navy-deep: #18318a;
    --veil: #5b68b6;
    --ink: #2b2b2b;
    --paper: #ffffff;
    --rule: #dcdcdc;
    --frame: #333333;
  }
  * { box-sizing: border-box; margin: 0; padding: 0; }
  html, body { width: 1200px; height: 600px; overflow: hidden; background: var(--paper); }
  .spread {
    position: relative; width: 1200px; height: 600px;
    border: 1px solid var(--frame); background: var(--paper);
    display: flex;
  }
  .panel {
    position: relative; width: 300px; height: 100%;
    border-right: 1px solid var(--rule);
  }
  .panel:last-child { border-right: none; }
  .header {
    position: absolute; top: 28px; left: 0; width: 100%; height: 135px;
  }
  .header .topline {
    position: absolute; top: 1px; left: 0; width: 100%; height: 1.5px; background: var(--navy);
  }
  .photo {
    position: absolute; top: 2px; left: 0; width: 165px; height: 133px;
  }
  .photo--sign { background: linear-gradient(110deg, #e2d9cc, #c9bcaa 70%, #b7a996); }
  .photo--team { background: linear-gradient(90deg, #efece6, #d8d4cc 40%, #3a3e4a 55%, #2f3340 80%, #e4e0d8); }
  .photo--meeting { background: linear-gradient(100deg, #4b5260, #a9b6c0 40%, #d7dde0 70%, #eef0f0); }
  .photo--pen { background: linear-gradient(120deg, #9a9a9a, #e4e4e4 45%, #b8b8b8 70%, #f0f0f0); }
  .veil {
    position: absolute; top: 0; left: 165px; width: 103px; height: 135px;
    background: linear-gradient(180deg, #6471bc, var(--veil));
  }
  .band {
    position: absolute; top: 0; left: 268px; width: 32px; height: 135px; background: var(--navy-deep);
  }
  .title {
    position: absolute; left: 170px; bottom: 5px;
    font-family: "Crimson Pro", Georgia, serif; font-size: 12px; line-height: 13.5px;
    color: #fff; letter-spacing: 0.6px; white-space: nowrap;
  }
  .panel:last-child .title { left: 170px; }
  .copy {
    position: absolute; top: 218px; left: 57px; width: 235px;
    font-family: "Barlow Semi Condensed", Arial, sans-serif; font-weight: 300;
    font-size: 8.3px; line-height: 11.6px; color: var(--ink);
  }
  .copy p + p { margin-top: 11.6px; }
  .copy .claim { color: var(--navy); font-weight: 500; }
  .values { position: absolute; top: 218px; left: 57px; width: 240px; }
  .value { margin-bottom: 9px; }
  .value h3 {
    font-family: "Crimson Pro", Georgia, serif; font-weight: 400;
    font-size: 11.8px; line-height: 14px; color: var(--navy); letter-spacing: 0.5px;
  }
  .value h3 .initial { font-size: 19px; letter-spacing: 0; }
  .value p {
    margin-left: 13px;
    font-family: "Barlow Semi Condensed", Arial, sans-serif; font-weight: 300;
    font-size: 8.3px; line-height: 11.6px; color: var(--ink);
  }
</style>
</head>
<body>
<div class="spread">

  <section class="panel">
    <div class="header">
      <div class="photo photo--sign" role="img" aria-label="Foto: Firmenschild an der Hausfassade"></div>
      <div class="veil"></div><div class="band"></div><div class="topline"></div>
      <h2 class="title">Unternehmen</h2>
    </div>
    <div class="copy">
      <p>Die SOLITAR Vermögensverwaltung GmbH ist eine<br>professionelle, unabhängige Vermögensverwaltung,<br>die maßgeschneiderte Anlage- und Depotstrategien für<br>Privatkunden und institutionelle Investoren entwickelt.<br>Dabei stehen die ganz persönlichen Zielvorstellungen der<br>Klienten stets im Vordergrund.</p>
      <p>Angeboten werden umfangreiche Dienstleistungen im<br>privaten und unternehmerischen Finanzmanagement,<br>von Vermögensübersichten und Einkommensplanungen<br>über Finanzierungskonzepte bis hin zu Family Office<br>Lösungen und Nachfolgeplanungen. Bei uns bekommen<br>Sie alles aus einer Hand.</p>
      <p class="claim">Individualität, Unabhängigkeit und Professionalität<br>sind nicht nur Worte, sondern gelebte Grundsätze</p>
    </div>
  </section>

  <section class="panel">
    <div class="header">
      <div class="photo photo--team" role="img" aria-label="Foto: zwei Geschäftsführer im Büro"></div>
      <div class="veil"></div><div class="band"></div><div class="topline"></div>
      <h2 class="title">Philosophie &amp;<br>Grundsätze</h2>
    </div>
    <div class="values">
      <div class="value"><h3><span class="initial">U</span>nabhängigkeit</h3><p>Wir sind bankenunabhängig und frei in der Auswahl<br>sämtlicher Anlageprodukte.</p></div>
      <div class="value"><h3><span class="initial">N</span>eutralität</h3><p>Wir garantieren eine absolut neutrale Betreuung,<br>die auf Ihre ganz persönlichen Bedürfnisse zuge-<br>schnitten ist.</p></div>
      <div class="value"><h3><span class="initial">I</span>ndividualität</h3><p>Wir richten unsere Tätigkeiten ausschließlich nach<br>Ihren Zielen und an Ihrer persönlichen Vermögens-<br>situation aus.</p></div>
      <div class="value"><h3><span class="initial">K</span>ompetenz</h3><p>Durch unsere langjährige Kapitalmarkterfahrung<br>zielen wir auf langfristigen Erfolg und Kapitalerhalt,<br>nicht auf kurzfristigen Profit.</p></div>
      <div class="value"><h3><span class="initial">A</span>ktivität</h3><p>Wir passen Ihre Vermögenswerte zeitnah und<br>konsequent an sich ändernde Rahmenbedingungen an.</p></div>
      <div class="value"><h3><span class="initial">T</span>ransparenz</h3><p>Wir informieren Sie in kurzen Zeitabständen<br>transparent und leicht verständlich über Ihre<br>Vermögensentwicklung.</p></div>
    </div>
  </section>

  <section class="panel">
    <div class="header">
      <div class="photo photo--meeting" role="img" aria-label="Foto: Beratungsgespräch am Glastisch"></div>
      <div class="veil"></div><div class="band"></div><div class="topline"></div>
      <h2 class="title">Anlagephilosophie</h2>
    </div>
    <div class="copy">
      <p>Jeder Anleger hat ganz individuelle Lebensumstände.<br>Die Berücksichtigung dieser spezifischen Rahmen-<br>bedingungen ist für eine erfolgreiche Kapitalanlage<br>unabdingbar. Die SOLITAR Vermögensverwaltung GmbH<br>bietet deshalb maßgeschneiderte Lösungen an, um<br>präzise auf die Wünsche Ihrer Mandanten einzugehen.</p>
      <p>Unsere Unabhängigkeit ist dabei unser Kapital.<br>Individuelle Anlage- und Depotstrategien sowie eine<br>bankenunabhängige Produktauswahl sind für uns<br>selbstverständlich. Dabei setzen wir auf langfristigen<br>Erfolg durch exzellente, bonitätsstarke Anlageinstrumente.</p>
      <p>Eine zeitnahe, regelmäßige und aussagefähige Bericht-<br>erstattung sorgt für Transparenz und Vertrauen.</p>
    </div>
  </section>

  <section class="panel">
    <div class="header">
      <div class="photo photo--pen" role="img" aria-label="Foto: Füllfederhalter mit goldener Feder"></div>
      <div class="veil"></div><div class="band"></div><div class="topline"></div>
      <h2 class="title">Vertragsgestaltung</h2>
    </div>
    <div class="copy">
      <p>So individuell wie wir Vermögen verwalten, so individuell<br>gestalten wir Verträge.</p>
      <p>Nach einem ausführlichen Beratungsgespräch wird<br>im Verwaltungsvertrag die Risikobereitschaft und die<br>Anlagestrategie festgehalten. Die SOLITAR Vermögens-<br>verwaltung GmbH erhält eine festgelegte Grundvergütung.<br>Die Höhe dieser Vergütung ist abhängig vom Umfang<br>des erteilten Verwaltungsauftrags.</p>
      <p>Darüber hinaus kann ein variables Erfolgshonorar,<br>das von den erwirtschafteten Renditen abhängig ist,<br>vereinbart werden.</p>
      <p>Die Verträge werden auf unbestimmte Zeit abgeschlossen,<br>sind jedoch jederzeit kündbar.</p>
    </div>
  </section>

</div>
</body>
</html>
```